Website banner

Here is the link where the current banner is featured https://www.brimlark.com.au/collections/gel-blasters

I need the banner recreated into desktop and mobile format size.
Update the key points to:
- FREE SHIPPING AUSTRALIA WIDE
- SAME DAY DISPATCH
- BEST PRICE GUARANTEE
- 3000+ 5 STAR REVIEWS
- BEST SERVICE & WARRANTY
- 100% SECURE CHECKOUT

I want the banner to suit the style of the website and make it look better than the last graphic.

I also need the "save even more" picture to be recreated as it looks very plain at the moment,

```html
<!DOCTYPE html>
<html lang="en">
<head>
<meta charset="utf-8">
<title>Gel Blasters Banner Set</title>
<link href="https://fonts.googleapis.com/css2?family=Montserrat:wght@800;900&display=swap" rel="stylesheet">
<style>
  :root {
    --page-bg: #ececec;
    --black: #0b0b0b;
    --black-soft: #1c1c1c;
    --red: #e8141b;
    --red-deep: #c9131a;
    --white: #ffffff;
  }
  html, body { margin: 0; padding: 0; overflow: hidden; }
  body {
    width: 1200px; height: 3094px; position: relative;
    background: var(--page-bg);
    font-family: "Montserrat", Arial, sans-serif;
  }
  .feature-strip {
    position: absolute; left: 0; top: 853px; width: 1200px; height: 182px;
    background: linear-gradient(135deg, var(--black-soft), var(--black) 50%, var(--black-soft));
    border-top: 3px solid var(--red);
    box-shadow: 0 8px 18px rgba(0,0,0,.25);
  }
  .feature-grid {
    position: absolute; left: 0; top: 1621px; width: 1200px; height: 757px;
    background: linear-gradient(160deg, var(--black-soft), var(--black) 45%, var(--black-soft));
  }
  .feature {
    position: absolute; transform: translateX(-50%);
    display: flex; flex-direction: column; align-items: center;
    text-align: center; font-weight: 900; text-transform: uppercase; white-space: nowrap;
  }
  .feature .line-top { color: var(--white); }
  .feature .line-bottom { color: var(--red); }
  .feature-strip .feature { top: 50px; font-size: 12px; line-height: 12px; }
  .feature-strip .feature svg { width: 46px; height: 46px; margin-bottom: 10px; }
  .feature-grid .feature { font-size: 28px; line-height: 28px; }
  .feature-grid .feature svg { width: 112px; height: 112px; margin-bottom: 22px; }
  .map-placeholder { fill: var(--red); }
  .savings-panel {
    position: absolute; left: 0; top: 2378px; width: 1200px; height: 716px;
    background: linear-gradient(150deg, var(--red), var(--red-deep) 50%, var(--red));
  }
  .savings-box {
    position: absolute; left: 156px; top: 126px; width: 887px; height: 457px;
    background: var(--black); border-bottom: 7px solid var(--red);
    box-shadow: 0 4px 0 rgba(0,0,0,.2);
    text-align: center;
  }
  .savings-title {
    margin: 34px 0 0; color: var(--red); font-size: 76px; font-weight: 900; letter-spacing: 1px; line-height: 1;
  }
  .savings-tier {
    margin: 0; color: var(--white); font-size: 46px; font-weight: 900; letter-spacing: 1px; line-height: 95px;
  }
  .savings-tier:first-of-type { margin-top: 24px; }
  .savings-tier .discount { color: var(--red); }
</style>
</head>
<body>

<svg width="0" height="0" style="position:absolute">
  <defs>
    <symbol id="icon-map" viewBox="0 0 100 100"><rect class="map-placeholder" x="8" y="12" width="84" height="70" rx="22"/></symbol>
    <symbol id="icon-plane" viewBox="0 0 100 100"><g fill="#e8141b">
      <path d="M30 45 L55 45 L40 20 L50 20 L72 45 L88 45 Q96 50 88 55 L72 55 L50 80 L40 80 L55 55 L30 55 Z"/>
      <rect x="8" y="38" width="16" height="5" rx="2"/><rect x="4" y="48" width="20" height="5" rx="2"/><rect x="8" y="58" width="16" height="5" rx="2"/></g></symbol>
    <symbol id="icon-stars" viewBox="0 0 100 100"><g fill="#e8141b">
      <path id="star" d="M0 -14 L4 -4 L14 -4 L6 3 L9 13 L0 7 L-9 13 L-6 3 L-14 -4 L-4 -4 Z" transform="translate(35 32)"/>
      <use href="#star" transform="translate(30 0)"/><use href="#star" transform="translate(-15 28)"/>
      <use href="#star" transform="translate(15 28)"/><use href="#star" transform="translate(45 28)"/></g></symbol>
    <symbol id="icon-thumb" viewBox="0 0 100 100"><g fill="#e8141b">
      <rect x="12" y="48" width="16" height="40" rx="3"/>
      <path d="M32 50 L48 28 Q54 20 58 30 L54 46 L80 46 Q88 48 86 56 Q90 62 84 66 Q88 72 80 76 Q82 86 72 86 L32 86 Z"/>
      <rect x="46" y="4" width="5" height="12" rx="2"/><rect x="30" y="12" width="5" height="10" rx="2" transform="rotate(-35 32 17)"/><rect x="64" y="12" width="5" height="10" rx="2" transform="rotate(35 66 17)"/></g></symbol>
    <symbol id="icon-tag" viewBox="0 0 100 100"><g transform="rotate(-45 50 50)">
      <path d="M22 36 L62 36 L82 50 L62 64 L22 64 Q16 64 16 58 L16 42 Q16 36 22 36 Z" fill="#e8141b"/>
      <circle cx="66" cy="50" r="4" fill="#0b0b0b"/>
      <text x="40" y="58" font-family="Montserrat, Arial, sans-serif" font-weight="900" font-size="22" fill="#0b0b0b" text-anchor="middle">$</text></g>
      <path d="M66 34 Q80 10 90 22 Q96 34 78 40" fill="none" stroke="#e8141b" stroke-width="5"/></symbol>
    <symbol id="icon-lock" viewBox="0 0 100 100"><g fill="#e8141b">
      <path d="M32 44 L32 32 Q32 12 50 12 Q68 12 68 32 L68 44 L60 44 L60 32 Q60 20 50 20 Q40 20 40 32 L40 44 Z"/>
      <rect x="24" y="44" width="52" height="46" rx="5"/></g>
      <circle cx="50" cy="62" r="6" fill="#0b0b0b"/><rect x="47" y="62" width="6" height="14" fill="#0b0b0b"/></symbol>
  </defs>
</svg>

<section class="feature-strip" aria-label="Store benefits, desktop">
  <div class="feature" style="left:240px"><svg role="img" aria-label="Map of Australia"><use href="#icon-map"/></svg><span class="line-top">Free Shipping</span><span class="line-bottom">Australia Wide</span></div>
  <div class="feature" style="left:370px"><svg><use href="#icon-plane"/></svg><span class="line-top">Same Day</span><span class="line-bottom">Dispatch</span></div>
  <div class="feature" style="left:490px"><svg><use href="#icon-tag"/></svg><span class="line-top">Best Price</span><span class="line-bottom">Guarantee</span></div>
  <div class="feature" style="left:651px"><svg><use href="#icon-stars"/></svg><span class="line-top">3000+ 5 Star</span><span class="line-bottom">Reviews</span></div>
  <div class="feature" style="left:824px"><svg><use href="#icon-thumb"/></svg><span class="line-top">Best Service</span><span class="line-bottom">&amp; Warranty</span></div>
  <div class="feature" style="left:969px"><svg><use href="#icon-lock"/></svg><span class="line-top">100% Secure</span><span class="line-bottom">Checkout</span></div>
</section>

<section class="feature-grid" aria-label="Store benefits, mobile">
  <div class="feature" style="left:256px;top:130px"><svg role="img" aria-label="Map of Australia"><use href="#icon-map"/></svg><span class="line-top">Free Shipping</span><span class="line-bottom">Australia Wide</span></div>
  <div class="feature" style="left:567px;top:130px"><svg><use href="#icon-plane"/></svg><span class="line-top">Same Day</span><span class="line-bottom">Dispatch</span></div>
  <div class="feature" style="left:907px;top:130px"><svg><use href="#icon-stars"/></svg><span class="line-top">3000+ 5 Star</span><span class="line-bottom">Reviews</span></div>
  <div class="feature" style="left:256px;top:418px"><svg><use href="#icon-thumb"/></svg><span class="line-top">Best Service</span><span class="line-bottom">&amp; Warranty</span></div>
  <div class="feature" style="left:567px;top:418px"><svg><use href="#icon-tag"/></svg><span class="line-top">Best Price</span><span class="line-bottom">Guarantee</span></div>
  <div class="feature" style="left:907px;top:418px"><svg><use href="#icon-lock"/></svg><span class="line-top">100% Secure</span><span class="line-bottom">Checkout</span></div>
</section>

<section class="savings-panel" aria-label="Bulk order discounts">
  <div class="savings-box">
    <h2 class="savings-title">SAVE EVEN MORE!</h2>
    <p class="savings-tier">ORDER $250+GET <span class="discount">5% OFF</span></p>
    <p class="savings-tier">ORDER $500+GET <span class="discount">10% OFF</span></p>
    <p class="savings-tier">ORDER $1000+GET <span class="discount">15% OFF</span></p>
  </div>
</section>

</body>
</html>
```